We need an email signature to highlight our brand, as well as include our product ranges. The brand has an Italian origin and we have a logo developed already.
For the email signature please include the following content:
Dean Mor | Partner
Email: Dean.mor@verastolo.com.au
Office: + 61 2 9481 7062
Mobile: + 61 438 915 264
Web: www.verastolo.com.au

Verastolo Lifestyle Centre:
Level 5, Brackley Design Centre
142 Pemberton Street, Waterloo
NSW 2017 Australia

[Product ranges] Kitchen Appliances | Designer Joineries | Blinds & Curtains | Fire Places | Featured Lightings | Smart Home | Bathroom Products

```html
<!DOCTYPE html>
<html lang="en">
<head>
<meta charset="utf-8">
<title>Verastolo – Email Signature Options</title>
<link rel="stylesheet" href="https://fonts.googleapis.com/css2?family=Arimo:wght@400;700&display=swap">
<style>
  :root{
    --page:#ececec;
    --card:#ffffff;
    --ink:#1e1e1e;
    --ink-soft:#2b2b2b;
    --accent-red:#c8102e;
    --rule:#1e1e1e;
    --placeholder:#d4d4d4;
    --frame:#ffffff;
  }
  *{box-sizing:border-box;margin:0;padding:0}
  html,body{width:1200px;height:619px;overflow:hidden;background:var(--page)}
  body{font-family:"Arimo",Arial,sans-serif;color:var(--ink)}
  .stage{position:relative;width:1431px;height:738px;transform:scale(0.83857);transform-origin:0 0}
  .signature{position:absolute;background:var(--card);box-shadow:0 1px 4px rgba(0,0,0,.08);overflow:hidden}
  .signature--kitchen-a{left:100px;top:100px;width:603px;height:264px}
  .signature--kitchen-b{left:728px;top:100px;width:603px;height:264px}
  .signature--wide{left:314px;top:414px;width:803px;height:224px}

  .brand{position:absolute;font-weight:700;font-size:34px;letter-spacing:-.5px;color:var(--ink);line-height:1}
  .signature--kitchen-a .brand,.signature--kitchen-b .brand{left:20px;top:42px}
  .signature--wide .brand{left:20px;top:88px}

  .person{position:absolute;font-size:16px;font-weight:700;color:var(--ink);white-space:nowrap}
  .person .role{font-size:11px;font-weight:400}
  .signature--kitchen-a .person,.signature--kitchen-b .person{left:20px;top:101px}
  .signature--wide .person{left:228px;top:58px}

  .contacts{position:absolute;list-style:none;font-size:11px;line-height:17px;color:var(--ink-soft)}
  .contacts li{display:flex;align-items:center;gap:4px;white-space:nowrap}
  .contacts svg{width:13px;height:13px;flex:none}
  .signature--kitchen-a .contacts,.signature--kitchen-b .contacts{left:20px;top:129px}
  .signature--wide .contacts{left:222px;top:86px}

  .address{position:absolute;font-style:normal;font-size:11px;line-height:17px;color:var(--ink-soft);white-space:nowrap}
  .address strong{font-weight:700}
  .signature--kitchen-a .address,.signature--kitchen-b .address{left:196px;top:129px}
  .signature--wide .address{left:398px;top:86px}

  .divider{position:absolute;height:1px;background:var(--rule)}
  .signature--kitchen-a .divider,.signature--kitchen-b .divider{left:20px;top:223px;width:323px}
  .signature--wide .divider{left:16px;top:190px;width:535px}

  .ranges{position:absolute;font-size:9.5px;line-height:14px;color:var(--ink)}
  .signature--kitchen-a .ranges,.signature--kitchen-b .ranges{left:20px;top:229px;width:330px}
  .signature--wide .ranges{left:20px;top:197px;white-space:nowrap}
  .ranges .dot{margin:0 4px}

  .photo{position:absolute;top:0;height:100%}
  .photo g{fill:var(--placeholder);stroke:var(--frame);stroke-width:7px}
  .signature--kitchen-a .photo,.signature--kitchen-b .photo{left:363px;width:240px}
  .signature--wide .photo{left:570px;width:233px}
</style>
</head>
<body>
<svg width="0" height="0" style="position:absolute" aria-hidden="true">
  <defs>
    <symbol id="icon-mail" viewBox="0 0 14 14"><circle cx="7" cy="7" r="6.2" fill="none" stroke="#1e1e1e" stroke-width="1.1"/><rect x="3.6" y="4.8" width="6.8" height="4.6" fill="#c8102e"/><path d="M3.6 4.8 7 7.6 10.4 4.8" fill="none" stroke="#fff" stroke-width=".8"/></symbol>
    <symbol id="icon-phone" viewBox="0 0 14 14"><circle cx="7" cy="7" r="6.2" fill="none" stroke="#1e1e1e" stroke-width="1.1"/><path d="M4.3 3.8c.5-.5 1-.4 1.3.1l.7 1.2c.2.4 0 .7-.3 1l-.4.3c.4.9 1 1.5 1.9 1.9l.3-.4c.3-.3.6-.5 1-.3l1.2.7c.5.3.6.8.1 1.3-.9.9-2.3.7-3.8-.6-1.6-1.4-2.9-3.6-2-4.2z" fill="#c8102e"/></symbol>
    <symbol id="icon-mobile" viewBox="0 0 14 14"><circle cx="7" cy="7" r="6.2" fill="none" stroke="#1e1e1e" stroke-width="1.1"/><rect x="4.7" y="3.3" width="4.6" height="7.4" rx=".8" fill="#c8102e"/><rect x="5.4" y="4.2" width="3.2" height="4.8" fill="#fff"/></symbol>
    <symbol id="icon-web" viewBox="0 0 14 14"><circle cx="7" cy="7" r="6.2" fill="none" stroke="#1e1e1e" stroke-width="1.1"/><circle cx="7" cy="7" r="3.6" fill="#c8102e"/><path d="M3.4 7h7.2M7 3.4v7.2M5.5 3.8c-1 2-1 4.4 0 6.4M8.5 3.8c1 2 1 4.4 0 6.4" fill="none" stroke="#fff" stroke-width=".6"/></symbol>
  </defs>
</svg>

<main class="stage">

  <section class="signature signature--kitchen-a">
    <div class="brand">Verastolo</div>
    <p class="person">Dean Mor <span class="role">/ Partner</span></p>
    <ul class="contacts">
      <li><svg><use href="#icon-mail"/></svg>Dean.mor@verastolo.com.au</li>
      <li><svg><use href="#icon-phone"/></svg>+ 61 2 9481 7062</li>
      <li><svg><use href="#icon-mobile"/></svg>+ 61 438 915 264</li>
      <li><svg><use href="#icon-web"/></svg>www.verastolo.com.au</li>
    </ul>
    <address class="address"><strong>Verastolo Lifestyle Centre</strong><br>Level 5, Brackley Design Centre<br>142 Pemberton Street, Waterloo<br>NSW 2017 Australia</address>
    <div class="divider"></div>
    <p class="ranges">Kitchen Appliances<span class="dot">•</span>Designer Joineries<span class="dot">•</span>Blinds &amp; Curtains<span class="dot">•</span>Fire Places<span class="dot">•</span>Featured Lightings<span class="dot">•</span>Smart Home<span class="dot">•</span>Bathroom Products</p>
    <svg class="photo" viewBox="0 0 240 264" role="img" aria-label="Kitchen interior photograph placeholder, framed in a honeycomb of hexagons">
      <g>
        <polygon points="30,-24 90,-24 120,28 90,80 30,80 0,28"/>
        <polygon points="30,80 90,80 120,132 90,184 30,184 0,132"/>
        <polygon points="30,184 90,184 120,236 90,288 30,288 0,236"/>
        <polygon points="120,28 180,28 210,80 180,132 120,132 90,80"/>
        <polygon points="120,132 180,132 210,184 180,236 120,236 90,184"/>
        <polygon points="120,-76 180,-76 210,-24 180,28 120,28 90,-24"/>
        <polygon points="120,236 180,236 210,288 180,340 120,340 90,288"/>
        <polygon points="210,-24 270,-24 300,28 270,80 210,80 180,28"/>
        <polygon points="210,80 270,80 300,132 270,184 210,184 180,132"/>
        <polygon points="210,184 270,184 300,236 270,288 210,288 180,236"/>
      </g>
    </svg>
  </section>

  <section class="signature signature--kitchen-b">
    <div class="brand">Verastolo</div>
    <p class="person">Dean Mor <span class="role">/ Partner</span></p>
    <ul class="contacts">
      <li><svg><use href="#icon-mail"/></svg>Dean.mor@verastolo.com.au</li>
      <li><svg><use href="#icon-phone"/></svg>+ 61 2 9481 7062</li>
      <li><svg><use href="#icon-mobile"/></svg>+ 61 438 915 264</li>
      <li><svg><use href="#icon-web"/></svg>www.verastolo.com.au</li>
    </ul>
    <address class="address"><strong>Verastolo Lifestyle Centre</strong><br>Level 5, Brackley Design Centre<br>142 Pemberton Street, Waterloo<br>NSW 2017 Australia</address>
    <div class="divider"></div>
    <p class="ranges">Kitchen Appliances<span class="dot">•</span>Designer Joineries<span class="dot">•</span>Blinds &amp; Curtains<span class="dot">•</span>Fire Places<span class="dot">•</span>Featured Lightings<span class="dot">•</span>Smart Home<span class="dot">•</span>Bathroom Products</p>
    <svg class="photo" viewBox="0 0 240 264" role="img" aria-label="Kitchen interior photograph placeholder, framed in staggered hexagons">
      <g>
        <polygon points="30,28 90,28 120,80 90,132 30,132 0,80"/>
        <polygon points="30,132 90,132 120,184 90,236 30,236 0,184"/>
        <polygon points="120,-24 180,-24 210,28 180,80 120,80 90,28"/>
        <polygon points="120,80 180,80 210,132 180,184 120,184 90,132"/>
        <polygon points="120,184 180,184 210,236 180,288 120,288 90,236"/>
        <polygon points="210,-76 270,-76 300,-24 270,28 210,28 180,-24"/>
        <polygon points="210,28 270,28 300,80 270,132 210,132 180,80"/>
        <polygon points="210,132 270,132 300,184 270,236 210,236 180,184"/>
        <polygon points="210,236 270,236 300,288 270,340 210,340 180,288"/>
      </g>
    </svg>
  </section>

  <section class="signature signature--wide">
    <div class="brand">Verastolo</div>
    <p class="person">Dean Mor <span class="role">/ Partner</span></p>
    <ul class="contacts">
      <li><svg><use href="#icon-mail"/></svg>Dean.mor@verastolo.com.au</li>
      <li><svg><use href="#icon-phone"/></svg>+ 61 2 9481 7062</li>
      <li><svg><use href="#icon-mobile"/></svg>+ 61 438 915 264</li>
      <li><svg><use href="#icon-web"/></svg>www.verastolo.com.au</li>
    </ul>
    <address class="address"><strong>Verastolo Lifestyle Centre</strong><br>Level 5, Brackley Design Centre<br>142 Pemberton Street, Waterloo<br>NSW 2017 Australia</address>
    <div class="divider"></div>
    <p class="ranges">Appliances<span class="dot">•</span>Designer Joineries<span class="dot">•</span>Blinds &amp; Curtains<span class="dot">•</span>Fire Places<span class="dot">•</span>Lightings<span class="dot">•</span>Smart Home<span class="dot">•</span>Bathroom Products</p>
    <svg class="photo" viewBox="0 0 233 224" role="img" aria-label="Dining room interior photograph placeholder, framed in hexagons">
      <g>
        <polygon points="28,4 86,4 114,58 86,112 28,112 0,58"/>
        <polygon points="28,112 86,112 114,166 86,220 28,220 0,166"/>
        <polygon points="114,-50 172,-50 200,4 172,58 114,58 86,4"/>
        <polygon points="114,58 172,58 200,112 172,166 114,166 86,112"/>
        <polygon points="114,166 172,166 200,220 172,274 114,274 86,220"/>
        <polygon points="200,4 258,4 286,58 258,112 200,112 172,58"/>
        <polygon points="200,112 258,112 286,166 258,220 200,220 172,166"/>
      </g>
    </svg>
  </section>

</main>
</body>
</html>
```